One-Page Redesign (Member's Area of Conference-Call Service)

Please take my mockup (THE ATTACHED PNG FILE) and make it look like a modern, cool, professional SaaS. Only restriction is you have to use free web fonts. And the fonts shouldn't have weird things like some letters or numbers being odd-sized.

If we work well together, I have an infinite amount of design projects for you to do.

Target Market(s)

Small Business Owners

Industry/Entity Type

Call

Number of Pages Required

1 page

Font styles to use
Sans Serif

Colors

Designer to choose colors to be used in the design.

Requirements
Must have
• It must look like a single, cohesive design -- with the menu and the content working together. It must be readable. It must be organized. It must give people an awesome first impression
Nice to have
• I'd like it to feel welcoming, not cold
Should not have
• It should not look like a damn template... It should not look amateurish

```html
<!DOCTYPE html>
<html lang="en">
<head>
<meta charset="utf-8">
<title>Account – Member Area</title>
<link rel="stylesheet" href="https://fonts.googleapis.com/css2?family=Roboto:wght@400;500;700&display=swap">
<style>
  :root {
    --side-bg: #3d4a66;
    --side-top: #2e3850;
    --side-line: #4c5875;
    --side-active: #4a6aa8;
    --ink: #3d4a66;
    --text: #3f3f46;
    --muted: #7a7a80;
    --page: #f3f3f3;
    --card: #ffffff;
    --card-line: #e4e4e6;
    --white: #ffffff;
  }
  * { box-sizing: border-box; margin: 0; padding: 0; }
  html, body { width: 1200px; height: 750px; overflow: hidden; }
  body {
    font-family: "Roboto", Arial, sans-serif;
    background: var(--page);
    color: var(--text);
    display: flex;
  }
  .sidebar {
    width: 235px;
    height: 750px;
    background: var(--side-bg);
    color: var(--white);
    flex-shrink: 0;
  }
  .brand {
    height: 104px;
    background: var(--side-top);
    display: flex;
    align-items: center;
    justify-content: center;
    gap: 10px;
  }
  .brand-dot { width: 18px; height: 18px; border-radius: 50%; background: var(--white); }
  .brand-name { font-size: 28px; font-weight: 700; letter-spacing: 0.5px; }
  .member {
    height: 90px;
    padding: 22px 9px 0;
    border-bottom: 1px solid var(--side-line);
  }
  .member-name { font-size: 23px; font-weight: 700; letter-spacing: 1px; }
  .member-id { font-size: 13px; font-weight: 700; letter-spacing: 0.6px; margin-top: 6px; }
  .nav { list-style: none; }
  .nav-item {
    height: 78.5px;
    display: flex;
    align-items: center;
    padding-left: 10px;
    gap: 11px;
    border-bottom: 1px solid var(--side-line);
    font-size: 13.5px;
    letter-spacing: 1px;
    font-weight: 500;
  }
  .nav-item--active { background: var(--side-active); border-bottom: none; height: 75px; }
  .nav-icon {
    width: 57px; height: 57px;
    background: var(--white);
    border-radius: 2px;
    display: flex; align-items: center; justify-content: center;
  }
  .nav-icon svg { width: 30px; height: 30px; stroke: var(--ink); fill: none; stroke-width: 1.6; }
  .main { flex: 1; height: 750px; }
  .topbar {
    height: 47px;
    background: var(--white);
    border-bottom: 1px solid var(--card-line);
    display: flex; align-items: center; justify-content: space-between;
    padding: 0 12px 0 13px;
  }
  .page-title { font-size: 17px; font-weight: 400; letter-spacing: 1.5px; color: #555; }
  .power svg { width: 20px; height: 20px; stroke: #666; fill: none; stroke-width: 2.2; stroke-linecap: round; }
  .breadcrumb { font-size: 11.5px; color: #555; padding: 22px 0 0 15px; height: 57px; letter-spacing: 0.3px; }
  .tiles {
    display: grid;
    grid-template-columns: repeat(3, 306px);
    grid-auto-rows: 193px;
    gap: 13px 12px;
    padding-left: 13px;
  }
  .tile {
    background: var(--card);
    border: 1px solid var(--card-line);
    text-align: center;
    padding: 25px 14px 0;
  }
  .tile--focus { border-color: #5b6478; box-shadow: 0 2px 8px rgba(0,0,0,0.12); }
  .tile-icon { width: 70px; height: 70px; margin: 0 auto; display: block; }
  .tile-title { font-size: 14px; font-weight: 500; letter-spacing: 1.3px; color: #444; margin-top: 20px; }
  .tile-text { font-size: 12.5px; line-height: 15px; letter-spacing: 0.5px; color: #444; margin-top: 15px; }
  .ic { stroke: var(--ink); fill: none; stroke-width: 4; stroke-linecap: round; stroke-linejoin: round; }
  .ic-fill { fill: var(--ink); }
  .ic-thin { stroke: var(--ink); fill: none; stroke-width: 2.6; stroke-linecap: round; stroke-linejoin: round; }
</style>
</head>
<body>
<svg width="0" height="0" style="position:absolute">
  <defs>
    <g id="sync-ring">
      <path class="ic" d="M14 28 A30 30 0 0 1 64 20"/>
      <path class="ic" d="M66 52 A30 30 0 0 1 16 60"/>
      <polygon class="ic-fill" points="6,22 20,20 14,34"/>
      <polygon class="ic-fill" points="74,58 60,60 66,46"/>
    </g>
  </defs>
</svg>

<aside class="sidebar">
  <div class="brand"><span class="brand-dot"></span><span class="brand-name">Callnest</span></div>
  <div class="member">
    <div class="member-name">Lorem Ipsum</div>
    <div class="member-id">Member ID:2102545</div>
  </div>
  <ul class="nav">
    <li class="nav-item">
      <span class="nav-icon"><svg viewBox="0 0 30 30"><path d="M9 5 l4 5 -2 3 c1 3 3 5 6 6 l3 -2 5 4 -2 4 c-8 0 -17 -9 -17 -17z"/><path d="M17 6 a7 7 0 0 1 7 7 M17 2 a11 11 0 0 1 11 11"/></svg></span>
      PHONE CONFRENCE
    </li>
    <li class="nav-item">
      <span class="nav-icon"><svg viewBox="0 0 30 30"><rect x="4" y="6" width="22" height="20"/><path d="M4 11 h22 M9 3 v5 M21 3 v5 M4 16 h22 M4 21 h22 M10 11 v15 M15 11 v15 M20 11 v15"/></svg></span>
      SCHEDULED EVENTS
    </li>
    <li class="nav-item">
      <span class="nav-icon"><svg viewBox="0 0 30 30"><path d="M15 9 l9 4 -9 4 -9 -4z M6 13 v9 l9 4 9 -4 v-9 M15 17 v9 M10 3 v4 M15 2 v4 M20 3 v4 M4 24 l-2 3 M26 24 l2 3"/></svg></span>
      COOL STUFF
    </li>
    <li class="nav-item">
      <span class="nav-icon"><svg viewBox="0 0 30 30"><path d="M10 10 a5 5 0 1 1 7 5 c-2 1 -2 3 -2 5" stroke-width="2.4"/><circle cx="15" cy="25" r="1.4" fill="#3d4a66"/></svg></span>
      HELP &amp; TRAINING
    </li>
    <li class="nav-item nav-item--active">
      <span class="nav-icon"><svg viewBox="0 0 30 30"><circle cx="15" cy="10" r="6"/><path d="M4 27 v-3 c0 -4 4 -7 11 -7 s11 3 11 7 v3z"/></svg></span>
      ACCOUNT
    </li>
  </ul>
</aside>

<main class="main">
  <header class="topbar">
    <h1 class="page-title">ACCOUNT</h1>
    <span class="power"><svg viewBox="0 0 20 20"><path d="M6 5 a7 7 0 1 0 8 0"/><path d="M10 2 v7"/></svg></span>
  </header>
  <nav class="breadcrumb">Home / Account</nav>

  <section class="tiles">
    <article class="tile tile--focus">
      <svg class="tile-icon" viewBox="0 0 80 80"><use href="#sync-ring"/><rect class="ic-thin" x="27" y="28" width="26" height="22"/><path class="ic-thin" d="M27 33 h26 M33 24 v6 M47 24 v6"/></svg>
      <h2 class="tile-title">CHANGE PLAN</h2>
      <p class="tile-text">Click here to change your service plan or cancel/ suspend service.</p>
    </article>
    <article class="tile">
      <svg class="tile-icon" viewBox="0 0 80 80"><use href="#sync-ring"/><circle class="ic" cx="31" cy="40" r="6"/><path class="ic" d="M37 40 h16 M47 40 v5 M52 40 v5"/></svg>
      <h2 class="tile-title">CHANGE PASSWORD</h2>
      <p class="tile-text">Click here to change your password.</p>
    </article>
    <article class="tile">
      <svg class="tile-icon" viewBox="0 0 80 80"><use href="#sync-ring"/><rect class="ic-thin" x="30" y="31" width="24" height="17"/><path class="ic-thin" d="M30 31 l12 9 12 -9 M20 38 h6 M22 43 h5"/></svg>
      <h2 class="tile-title">CHANGE EMAIL</h2>
      <p class="tile-text">Click here to change your email assoclaged with the account.</p>
    </article>
    <article class="tile">
      <svg class="tile-icon" viewBox="0 0 80 80"><use href="#sync-ring"/><rect class="ic-thin" x="26" y="30" width="28" height="20"/><circle class="ic-fill" cx="34" cy="38" r="3"/><path class="ic-fill" d="M29 46 c0 -4 10 -4 10 0z"/><path class="ic-thin" d="M42 37 h8 M42 42 h8"/></svg>
      <h2 class="tile-title">CHANGE BILLING INFO</h2>
      <p class="tile-text">Click here to update or change the credit card on file for your account.</p>
    </article>
    <article class="tile">
      <svg class="tile-icon" viewBox="0 0 80 80"><circle class="ic" cx="40" cy="40" r="33"/><path class="ic-thin" d="M34 26 h12 l6 6 v22 h-18 v-9 M46 26 v6 h6 M40 34 h8 M40 39 h8 M40 44 h8 M40 49 h8"/><path class="ic-thin" d="M28 48 l3 3 6 -7"/></svg>
      <h2 class="tile-title">VIEW INVOICES</h2>
      <p class="tile-text">Click here to view previously paid invoices.</p>
    </article>
    <article class="tile">
      <svg class="tile-icon" viewBox="0 0 80 80"><circle class="ic" cx="40" cy="40" r="33"/><circle class="ic-fill" cx="33" cy="34" r="6"/><circle class="ic-fill" cx="47" cy="34" r="6"/><path class="ic-fill" d="M22 52 c0 -8 6 -11 11 -11 s11 3 11 11z M36 52 c0 -8 6 -11 11 -11 s11 3 11 11z"/></svg>
      <h2 class="tile-title">AFFILIATES</h2>
      <p class="tile-text">Click here get information about your affilate account and how to earn money promoting ConferLine.</p>
    </article>
  </section>
</main>
</body>
</html>
```